Flight school needs business cards!

We need a cool business card design for two flight school employees. The Chief Flight Instructor and the Manager. Put simply, we teach people how to fly. I would think it would be cool to have the front of the business card look like a pilot's license (US pilot certificate) and the backside has the logo and contact information.

Target Market(s)

Someone who wants to learn how to fly.

Industry/Entity Type

Aviation

Requirements
Must have
• The front of the business card should look like a United States pilot license, and it should read:

Your Name Here
Your Address Here

DOB and other personal information should be left plank.

Then under where it says
"Has been found to be properly qualified to exercise the privileges of
It should say Sport Pilot
Private Pilot
Commercial pilot

Basically, it is a way of saying what types of pilot licenses we can train someone for, and should be motivating for someone to have in their wallet. Something they don't want to throw away

```html
<!DOCTYPE html>
<html lang="en">
<head>
<meta charset="utf-8">
<title>Zenith Aviation – Business Cards</title>
<link href="https://fonts.googleapis.com/css2?family=Michroma&family=Roboto:wght@400;500&display=swap" rel="stylesheet">
<style>
  :root {
    --page-bg: #e9edf2;
    --card-top: #f7f8fc;
    --card-bottom: #e4eaf3;
    --scene-sky: #dfe6f2;
    --scene-ground: #c9d6e6;
    --navy: #101b36;
    --ink: #1d2330;
    --red: #e2231a;
    --faint-red: #f3c9c0;
  }
  * { box-sizing: border-box; margin: 0; padding: 0; }
  html, body { width: 800px; height: 1200px; overflow: hidden; }
  body {
    background: var(--page-bg);
    font-family: "Roboto", Arial, sans-serif;
    color: var(--ink);
    position: relative;
  }
  .card {
    position: absolute;
    left: 150px;
    width: 500px;
    height: 285px;
    border-radius: 12px;
    overflow: hidden;
    background: linear-gradient(180deg, var(--card-top) 0%, var(--card-bottom) 100%);
    box-shadow: 0 4px 14px rgba(16, 27, 54, 0.15);
  }
  .card--contact { top: 135px; }
  .card--certificate { top: 735px; }

  .scene-art {
    position: absolute;
    inset: 0;
    background:
      radial-gradient(ellipse 55% 60% at 75% 35%, rgba(243, 201, 192, 0.35), transparent 70%),
      linear-gradient(180deg, rgba(223, 230, 242, 0) 40%, var(--scene-sky) 75%, var(--scene-ground) 100%);
  }

  /* Front: logo area */
  .brand-seal {
    position: absolute;
    left: 44px;
    top: 42px;
    width: 198px;
    height: 198px;
    border-radius: 50%;
    background: #ffffff;
    border: 4px solid var(--red);
    display: flex;
    align-items: center;
    justify-content: center;
    text-align: center;
  }
  .brand-seal__name {
    font-family: "Roboto", Arial, sans-serif;
    font-weight: 500;
    font-size: 20px;
    line-height: 1.25;
    letter-spacing: 1px;
    color: var(--navy);
  }

  .person {
    position: absolute;
    left: 285px;
    top: 34px;
  }
  .person__name {
    font-family: "Michroma", Arial, sans-serif;
    font-size: 15px;
    color: var(--navy);
    letter-spacing: 0.5px;
    line-height: 20px;
  }
  .person__role {
    font-size: 11px;
    color: var(--red);
    letter-spacing: 0.4px;
    line-height: 14px;
  }

  .contact-list {
    position: absolute;
    left: 285px;
    top: 155px;
    list-style: none;
    font-size: 11px;
    color: var(--ink);
  }
  .contact-list li {
    display: flex;
    align-items: flex-start;
    line-height: 15.5px;
  }
  .contact-list svg {
    width: 9px;
    height: 9px;
    margin: 3px 9px 0 0;
    flex: none;
  }

  /* Back: certificate */
  .cert-title {
    position: absolute;
    left: 0;
    right: 0;
    top: 14px;
    text-align: center;
    font-family: "Michroma", Arial, sans-serif;
    font-size: 18px;
    color: var(--ink);
    letter-spacing: 0.5px;
  }
  .cert-subtitle {
    position: absolute;
    left: 0;
    right: 0;
    top: 39px;
    text-align: center;
    font-size: 11px;
    font-weight: 500;
    letter-spacing: 0.3px;
  }
  .cert-field {
    position: absolute;
    font-size: 11.5px;
    font-weight: 500;
    text-transform: uppercase;
    color: var(--ink);
    white-space: nowrap;
    line-height: 14px;
  }
  .cert-field__no {
    display: inline-block;
    min-width: 24px;
  }
  .cert-traits {
    position: absolute;
    top: 147px;
    left: 228px;
    display: flex;
    font-size: 11.5px;
    font-weight: 500;
    text-transform: uppercase;
  }
  .cert-traits span {
    padding: 0 10px 0 12px;
    border-left: 1px solid rgba(29, 35, 48, 0.45);
  }
  .cert-traits span:first-child { border-left: none; }
  .cert-seal {
    position: absolute;
    left: 353px;
    top: 205px;
    width: 68px;
    height: 67px;
    border-radius: 2px;
    background: linear-gradient(135deg, #f7c7e0, #c9e7f7 30%, #f8f1b4 55%, #c8f0cf 75%, #e5c7f7);
  }
</style>
</head>
<body>

  <section class="card card--contact">
    <div class="scene-art" role="img" aria-label="Faint background illustration of a vintage biplane, a jet and a standing pilot"></div>

    <div class="brand-seal">
      <span class="brand-seal__name">ZENITH<br>AVIATION</span>
    </div>

    <div class="person">
      <h1 class="person__name">MARK ELLISON</h1>
      <p class="person__role">MANAGER</p>
      <p class="person__role">CHIEF FLIGHT INSTRUCTOR</p>
    </div>

    <ul class="contact-list">
      <li>
        <svg viewBox="0 0 10 10"><path fill="#e2231a" d="M2 0.5l1.6 2-1 1.1c.6 1.3 1.6 2.3 2.8 2.8l1.1-1 2 1.6-.9 1.8C4.3 8.6 1.4 5.7.4 2z"/></svg>
        <span>(03) 5550 1842</span>
      </li>
      <li>
        <svg viewBox="0 0 10 10"><rect x="0" y="1.5" width="10" height="7" fill="#e2231a"/><path d="M0.5 2l4.5 3.5L9.5 2" stroke="#fff" stroke-width="1" fill="none"/></svg>
        <span>mark@zenithaviation.com</span>
      </li>
      <li>
        <svg viewBox="0 0 10 10"><g fill="none" stroke="#e2231a" stroke-width="0.9"><circle cx="5" cy="5" r="4.4"/><ellipse cx="5" cy="5" rx="2" ry="4.4"/><path d="M0.6 5h8.8M1.3 2.8h7.4M1.3 7.2h7.4"/></g></svg>
        <span>www.zenithaviation.com</span>
      </li>
      <li>
        <svg viewBox="0 0 10 10"><path fill="#e2231a" d="M5 0a3.6 3.6 0 0 0-3.6 3.6C1.4 6.3 5 10 5 10s3.6-3.7 3.6-6.4A3.6 3.6 0 0 0 5 0zm0 5.1a1.5 1.5 0 1 1 0-3 1.5 1.5 0 0 1 0 3z"/></svg>
        <span>118 Harbor Lane<br>Suite 210, Fairview<br>MI 49000</span>
      </li>
    </ul>
  </section>

  <section class="card card--certificate">
    <div class="scene-art" role="img" aria-label="Faint background illustration of a vintage biplane, a jet and a standing pilot"></div>

    <span class="cert-field" style="left:24px; top:19px;">I</span>
    <h2 class="cert-title">ZENITH AVIATION</h2>
    <p class="cert-subtitle">FLIGHT SCHOOL</p>

    <p class="cert-field" style="left:24px; top:55px;"><span class="cert-field__no">IV</span>Your Name Here</p>
    <p class="cert-field" style="left:24px; top:96px;"><span class="cert-field__no">V</span>Your Address Here</p>

    <div class="cert-traits">
      <span>Sex</span><span>Height</span><span>Weight</span><span>Hair</span><span>Eyes</span>
    </div>

    <p class="cert-field" style="left:24px; top:160px;"><span class="cert-field__no">VI</span>D.O.B</p>
    <p class="cert-field" style="left:24px; top:182px;"><span class="cert-field__no">IVa</span>Has been found to be properly qualified to exercise the privileges of</p>
    <p class="cert-field" style="left:49px; top:205px;">IX&nbsp;&nbsp;It should say Sport Pilot</p>
    <p class="cert-field" style="left:49px; top:224px;">II&nbsp;&nbsp;&nbsp;Private Pilot</p>
    <p class="cert-field" style="left:49px; top:244px;">III&nbsp;&nbsp;Commercial Pilot</p>

    <div class="cert-seal" role="img" aria-label="Holographic security seal"></div>
  </section>

</body>
</html>
```